Concert Poster

Needing a concert poster featuring two different artist Dane Holloway and Jonas Pryce.
It is a free event sponsored by Gathered Hearts on The Hill and the Circle of Kindred.
Date: Saturday June 8th
Location: Marbury High Football Field
Address: 718 S Falcon Pkwy Marbury, TN

```html
<!DOCTYPE html>
<html lang="en">
<head>
<meta charset="utf-8">
<title>Concert Poster – Gathered Hearts on The Hill</title>
<link rel="stylesheet" href="https://fonts.googleapis.com/css2?family=Roboto+Slab:wght@800&family=Lora:ital,wght@0,400;1,500&family=Pinyon+Script&family=Kaushan+Script&display=swap">
<style>
  :root {
    --page-bg: #ececec;
    --ink-black: #050308;
    --night-purple: #3a1f6e;
    --glow-violet: #7a4fd0;
    --amber: #f39a2b;
    --amber-deep: #d97a12;
    --gold: #e8b54a;
    --gold-light: #fff0b8;
    --cream: #fff3d6;
    --silver: #d9dce3;
    --denim: #5d6f8c;
    --denim-dark: #2b3446;
    --shirt-dark: #2a2a30;
    --skin-warm: #9a7562;
    --white: #ffffff;
  }
  * { margin: 0; padding: 0; box-sizing: border-box; }
  html, body {
    width: 1200px; height: 651px; overflow: hidden;
    background: var(--page-bg);
  }
  .poster {
    position: absolute; left: 384px; top: 20px;
    width: 432px; height: 611px; overflow: hidden;
    background: var(--ink-black);
  }
  .poster__backdrop {
    position: absolute; inset: 0;
    background:
      radial-gradient(ellipse 60% 35% at 55% 10%, rgba(122,79,208,.8), transparent 70%),
      radial-gradient(ellipse 90% 18% at 50% 46%, rgba(170,90,160,.55), transparent 70%),
      linear-gradient(180deg, #0b0612 0%, var(--night-purple) 28%, #2c1640 45%, #1a0e16 62%, var(--ink-black) 78%);
  }
  .sponsor-mark {
    position: absolute; left: 34px; top: 70px;
    width: 26px; height: 26px; border-radius: 50%;
    background: var(--white);
  }
  .sponsor-label {
    position: absolute; left: 86px; top: 26px;
    font: italic 500 15px/1 "Lora", serif; color: var(--amber);
  }
  .sponsor-name {
    position: absolute; left: 85px; top: 46px;
    font: 800 29px/1 "Roboto Slab", serif; color: var(--white);
  }
  .connector {
    position: absolute; left: 86px; top: 92px;
    font: italic 500 18px/1 "Lora", serif; color: var(--amber);
  }
  .event-title {
    position: absolute; left: 82px; top: 116px;
    font: italic 500 38px/42px "Lora", serif; color: var(--cream);
    text-shadow: 0 0 6px rgba(243,154,43,.95), 0 0 14px rgba(243,154,43,.6);
  }
  .artist-photo {
    position: absolute;
    -webkit-mask-image: linear-gradient(180deg, #000 75%, transparent 100%);
            mask-image: linear-gradient(180deg, #000 75%, transparent 100%);
  }
  .artist-photo--left {
    left: 8px; top: 266px; width: 240px; height: 200px;
    border-radius: 60px 60px 0 0;
    background: linear-gradient(160deg, var(--denim) 0%, var(--denim-dark) 55%, #16131c 100%);
  }
  .artist-photo--right {
    left: 262px; top: 254px; width: 170px; height: 210px;
    border-radius: 70px 0 0 0;
    background: linear-gradient(175deg, #3b3b42 0%, var(--skin-warm) 30%, var(--shirt-dark) 60%, #121014 100%);
  }
  .artist-name { position: absolute; }
  .artist-name__first {
    display: block;
    font: 400 50px/1 "Pinyon Script", cursive; color: var(--silver);
    text-shadow: 0 1px 0 #8a8f99, 0 0 10px rgba(160,200,255,.5);
  }
  .artist-name__last {
    position: absolute; white-space: nowrap;
    font: 400 24px/1 "Kaushan Script", cursive; color: var(--amber);
  }
  .artist-name--left { left: 20px; top: 420px; }
  .artist-name--left .artist-name__last { left: 118px; top: 38px; }
  .artist-name--right { left: 268px; top: 414px; }
  .artist-name--right .artist-name__last { left: 72px; top: 42px; }
  .music-flourish {
    position: absolute; left: 34px; top: 486px; width: 262px; height: 62px;
    border-radius: 6px;
    background: linear-gradient(90deg, rgba(232,181,74,.55) 0%, rgba(184,128,40,.35) 45%, rgba(232,181,74,.2) 100%);
  }
  .venue-band { position: absolute; left: 0; bottom: 0; width: 432px; height: 72px; }
  .venue-list {
    position: absolute; left: 100px; top: 560px; list-style: none;
    font: italic 500 11.5px/21px "Lora", serif; color: var(--ink-black);
  }
  .venue-list li { display: flex; align-items: center; gap: 10px; }
  .venue-list svg { width: 10px; height: 13px; flex: none; }
  .date-badge {
    position: absolute; left: 302px; top: 484px;
    width: 110px; height: 110px; border-radius: 50%;
    background: radial-gradient(circle, var(--ink-black) 60%, var(--gold) 62%, var(--gold-light) 68%, var(--amber-deep) 74%, var(--gold) 80%, rgba(0,0,0,0) 82%);
    text-align: center; color: var(--white);
  }
  .date-badge__day {
    position: absolute; left: 0; right: 0; top: 22px;
    font: 800 36px/1 "Roboto Slab", serif;
  }
  .date-badge__day sup { font-size: 14px; vertical-align: top; }
  .date-badge__month {
    position: absolute; left: 0; right: 0; top: 61px;
    font: 400 21px/1 "Lora", serif; color: var(--amber); letter-spacing: 1px;
  }
  .date-badge__weekday {
    position: absolute; left: 0; right: 0; top: 81px;
    font: 400 7px/1 "Lora", serif; letter-spacing: .5px;
  }
</style>
</head>
<body>
  <main class="poster">
    <div class="poster__backdrop" role="img" aria-label="Night stadium with purple stage lights over the football field"></div>

    <div class="sponsor-mark"></div>
    <p class="sponsor-label">Sponsored by</p>
    <h2 class="sponsor-name">Gathered Hearts</h2>
    <p class="connector">on</p>
    <h1 class="event-title">The Hill<br>and the Circle<br>of Kindred</h1>

    <div class="artist-photo artist-photo--left" role="img" aria-label="Photo of Jonas Pryce in a denim jacket singing with an acoustic guitar"></div>
    <div class="artist-photo artist-photo--right" role="img" aria-label="Portrait photo of Dane Holloway in a cap and dark shirt"></div>

    <p class="artist-name artist-name--left"><span class="artist-name__first">Jonas</span><span class="artist-name__last">Pryce</span></p>
    <p class="artist-name artist-name--right"><span class="artist-name__first">Dane</span><span class="artist-name__last">Holloway</span></p>

    <div class="music-flourish" role="img" aria-label="Golden treble clef, music notes and sparkles decoration"></div>

    <svg class="venue-band" viewBox="0 0 432 72" preserveAspectRatio="none" aria-hidden="true">
      <path d="M0 60 Q110 4 300 2 Q360 28 412 72 L0 72 Z" fill="var(--amber)"/>
    </svg>

    <ul class="venue-list">
      <li><svg viewBox="0 0 10 13"><path d="M5 0a5 5 0 0 0-5 5c0 3.5 5 8 5 8s5-4.5 5-8a5 5 0 0 0-5-5zm0 7a2 2 0 1 1 0-4 2 2 0 0 1 0 4z" fill="var(--ink-black)"/></svg>Marbury High Football Field</li>
      <li><svg viewBox="0 0 10 13"><path d="M5 0a5 5 0 0 0-5 5c0 3.5 5 8 5 8s5-4.5 5-8a5 5 0 0 0-5-5zm0 7a2 2 0 1 1 0-4 2 2 0 0 1 0 4z" fill="var(--ink-black)"/></svg>718 S Falcon Pkwy Marbury, TN</li>
    </ul>

    <div class="date-badge">
      <span class="date-badge__day">8<sup>th</sup></span>
      <span class="date-badge__month">JUNE</span>
      <span class="date-badge__weekday">SATURDAY</span>
    </div>
  </main>
</body>
</html>
```